Verdant Solutions Business Card

want the back of card to be blue- with the logo in the center
front of card- info plus logo (info being mailing address, email address, and website address )
4 different names with titles to have on cards
1) Dalton Mirsky - Owner
2) Brenda Tolvin- Customer Relationship Specialist
3) Henri Kastner- Vice President of Sales
4) Wade Dunmor- Chief Technology Officer

Target Market(s)

tech company in the government/probation office industry

Industry/Entity Type

Government Office

Contact Information for Business Card

1) Dalton Mirsky - Owner

Colors
0355a3
ffffff

Requirements
Must have
• back side should be blue, with the logo placed in the center
• front side needs to include both the logo, as well as company info (info should include website address, email address, and mailing address)

```html
<!DOCTYPE html>
<html lang="en">
<head>
<meta charset="utf-8">
<title>Verdant Solutions Business Cards</title>
<link rel="stylesheet" href="https://fonts.googleapis.com/css2?family=Open+Sans:wght@400;600;700&family=Raleway:wght@400&display=swap">
<style>
  :root {
    --brand-blue: #0355a3;
    --navy: #1f2d5a;
    --white: #ffffff;
    --card-edge: #8a8a8a;
  }
  * { box-sizing: border-box; margin: 0; padding: 0; }
  html, body { width: 1200px; height: 1200px; overflow: hidden; background: var(--white); }
  .sheet { position: relative; width: 1200px; height: 1200px; }

  .card {
    position: absolute;
    width: 317px;
    height: 181px;
    overflow: hidden;
  }
  .card-front { background: var(--white); border: 1px solid var(--card-edge); }
  .card-back { background: var(--brand-blue); border: 1px solid var(--navy); }

  .name-pill {
    position: absolute;
    left: 0;
    top: 47px;
    height: 23px;
    padding: 0 13px 0 31px;
    background: var(--brand-blue);
    border-radius: 0 12px 12px 0;
    color: var(--white);
    font: 700 9.5px/23px "Open Sans", sans-serif;
    text-transform: uppercase;
    white-space: nowrap;
  }
  .job-title {
    position: absolute;
    left: 31px;
    top: 73px;
    color: var(--brand-blue);
    font: 400 7.5px/1 "Raleway", sans-serif;
    white-space: nowrap;
  }
  .contact-list { position: absolute; left: 29px; top: 100px; list-style: none; }
  .contact-item {
    display: flex;
    align-items: center;
    height: 12px;
    margin-bottom: 6px;
    color: var(--brand-blue);
    font: 600 7px/1 "Open Sans", sans-serif;
    white-space: nowrap;
  }
  .contact-icon { width: 11px; height: 11px; margin-right: 6px; flex: none; }

  .wordmark {
    position: absolute;
    text-align: center;
    color: var(--navy);
    font-family: "Open Sans", sans-serif;
    font-weight: 700;
    line-height: 1;
    text-transform: uppercase;
  }
  .card-front .wordmark { left: 190px; top: 68px; width: 120px; font-size: 16px; }
  .card-front .wordmark span { display: block; font-size: 10.5px; letter-spacing: 2.6px; margin-top: 4px; }
  .card-back .wordmark { left: 0; top: 62px; width: 100%; font-size: 32px; }
  .card-back .wordmark span { display: block; font-size: 20px; letter-spacing: 6px; margin-top: 6px; }
</style>
</head>
<body>
<main class="sheet">

  <!-- Brenda Tolvin -->
  <section class="card card-front" style="left:231px;top:173px">
    <div class="name-pill">Brenda Tolvin</div>
    <p class="job-title">Customer Relationship Specialist</p>
    <ul class="contact-list">
      <li class="contact-item"><svg class="contact-icon" viewBox="0 0 12 12"><circle cx="6" cy="6" r="6" fill="#0355a3"/><rect x="3" y="4" width="6" height="4.2" fill="#fff"/><path d="M3 4l3 2.3L9 4" stroke="#0355a3" stroke-width=".7" fill="none"/></svg>Support@VerdantSolutions.com</li>
      <li class="contact-item"><svg class="contact-icon" viewBox="0 0 12 12"><circle cx="6" cy="6" r="6" fill="#0355a3"/><circle cx="6" cy="6" r="3.2" fill="none" stroke="#fff" stroke-width=".8"/><path d="M6 2.8v6.4M2.8 6h6.4" stroke="#fff" stroke-width=".7"/></svg>www.VerdantSolutions.com</li>
    </ul>
    <div class="wordmark">Verdant<span>Solutions</span></div>
  </section>
  <section class="card card-back" style="left:231px;top:376px">
    <div class="wordmark">Verdant<span>Solutions</span></div>
  </section>

  <!-- Henri Kastner -->
  <section class="card card-front" style="left:694px;top:173px">
    <div class="name-pill">Henri Kastner</div>
    <p class="job-title">Vice President of Sales</p>
    <ul class="contact-list">
      <li class="contact-item"><svg class="contact-icon" viewBox="0 0 12 12"><circle cx="6" cy="6" r="6" fill="#0355a3"/><rect x="3" y="4" width="6" height="4.2" fill="#fff"/><path d="M3 4l3 2.3L9 4" stroke="#0355a3" stroke-width=".7" fill="none"/></svg>Support@VerdantSolutions.com</li>
      <li class="contact-item"><svg class="contact-icon" viewBox="0 0 12 12"><circle cx="6" cy="6" r="6" fill="#0355a3"/><circle cx="6" cy="6" r="3.2" fill="none" stroke="#fff" stroke-width=".8"/><path d="M6 2.8v6.4M2.8 6h6.4" stroke="#fff" stroke-width=".7"/></svg>www.VerdantSolutions.com</li>
    </ul>
    <div class="wordmark">Verdant<span>Solutions</span></div>
  </section>
  <section class="card card-back" style="left:694px;top:376px">
    <div class="wordmark">Verdant<span>Solutions</span></div>
  </section>

  <!-- Dalton Mirsky -->
  <section class="card card-front" style="left:231px;top:633px">
    <div class="name-pill">Dalton Mirsky</div>
    <p class="job-title">Owner</p>
    <ul class="contact-list">
      <li class="contact-item"><svg class="contact-icon" viewBox="0 0 12 12"><circle cx="6" cy="6" r="6" fill="#0355a3"/><rect x="3" y="4" width="6" height="4.2" fill="#fff"/><path d="M3 4l3 2.3L9 4" stroke="#0355a3" stroke-width=".7" fill="none"/></svg>Support@VerdantSolutions.com</li>
      <li class="contact-item"><svg class="contact-icon" viewBox="0 0 12 12"><circle cx="6" cy="6" r="6" fill="#0355a3"/><circle cx="6" cy="6" r="3.2" fill="none" stroke="#fff" stroke-width=".8"/><path d="M6 2.8v6.4M2.8 6h6.4" stroke="#fff" stroke-width=".7"/></svg>www.VerdantSolutions.com</li>
    </ul>
    <div class="wordmark">Verdant<span>Solutions</span></div>
  </section>
  <section class="card card-back" style="left:231px;top:835px">
    <div class="wordmark">Verdant<span>Solutions</span></div>
  </section>

  <!-- Wade Dunmor -->
  <section class="card card-front" style="left:694px;top:633px">
    <div class="name-pill">Wade Dunmor</div>
    <p class="job-title">Chief Technology Officer</p>
    <ul class="contact-list">
      <li class="contact-item"><svg class="contact-icon" viewBox="0 0 12 12"><circle cx="6" cy="6" r="6" fill="#0355a3"/><rect x="3" y="4" width="6" height="4.2" fill="#fff"/><path d="M3 4l3 2.3L9 4" stroke="#0355a3" stroke-width=".7" fill="none"/></svg>Support@VerdantSolutions.com</li>
      <li class="contact-item"><svg class="contact-icon" viewBox="0 0 12 12"><circle cx="6" cy="6" r="6" fill="#0355a3"/><circle cx="6" cy="6" r="3.2" fill="none" stroke="#fff" stroke-width=".8"/><path d="M6 2.8v6.4M2.8 6h6.4" stroke="#fff" stroke-width=".7"/></svg>www.VerdantSolutions.com</li>
    </ul>
    <div class="wordmark">Verdant<span>Solutions</span></div>
  </section>
  <section class="card card-back" style="left:694px;top:835px">
    <div class="wordmark">Verdant<span>Solutions</span></div>
  </section>

</main>
</body>
</html>
```